Wexley Foot & Ankle Halverton Window Vinyl Cling

Hi,
I'm looking to get a window decal done, but need it professionally designed.
-must be 24" x 24"
-Quorum Font
-Include our logo, Podiatry, phone number and website
- The goal is to make this eye catching.
Thank you,
Dorian

```html
<!DOCTYPE html>
<html lang="en">
<head>
<meta charset="utf-8">
<title>Wexley Foot &amp; Ankle Halverton – Window Cling</title>
<link rel="stylesheet" href="https://fonts.googleapis.com/css2?family=Rokkitt:wght@600;700;800&family=Poppins:wght@600&display=swap">
<style>
  :root {
    --orange: #f47e4a;
    --teal: #55c3a7;
    --teal-dark: #27886f;
    --ink: #1f1f1f;
    --paper: #ffffff;
    --backdrop: #5b5b5b;
  }
  html, body {
    margin: 0;
    padding: 0;
    width: 1200px;
    height: 2400px;
    overflow: hidden;
    background: var(--backdrop);
  }
  .decal {
    position: absolute;
    left: 80px;
    top: 680px;
    width: 1040px;
    height: 1040px;
    background: var(--paper);
    box-shadow: 0 6px 24px rgba(0,0,0,0.35);
    overflow: hidden;
    font-family: "Rokkitt", serif;
  }
  .brand {
    position: absolute;
    left: 90px;
    top: 60px;
    width: 860px;
    height: 240px;
    display: flex;
    align-items: center;
    gap: 30px;
  }
  .brand-dot {
    width: 220px;
    height: 220px;
    border-radius: 50%;
    background: var(--teal);
    flex: none;
  }
  .brand-name {
    margin: 0;
    color: var(--orange);
    font-weight: 700;
    font-size: 84px;
    line-height: 0.92;
    text-align: right;
    flex: 1;
  }
  .headline {
    position: absolute;
    left: 0;
    right: 0;
    margin: 0;
    text-align: center;
    line-height: 1;
  }
  .headline-service {
    top: 330px;
    color: var(--orange);
    font-weight: 700;
    font-size: 196px;
    letter-spacing: 2px;
  }
  .headline-specialty {
    top: 490px;
    color: var(--teal);
    font-weight: 700;
    font-size: 124px;
    letter-spacing: 1px;
  }
  .headline-role {
    top: 598px;
    color: var(--ink);
    font-family: "Poppins", sans-serif;
    font-weight: 600;
    font-size: 108px;
    letter-spacing: 8px;
  }
  .phone-pill {
    position: absolute;
    left: 66px;
    top: 757px;
    width: 886px;
    height: 113px;
    border-radius: 22px;
    background: var(--orange);
    box-shadow: 0 4px 6px rgba(0,0,0,0.18);
    display: flex;
    align-items: center;
    gap: 32px;
    padding-left: 28px;
    box-sizing: border-box;
  }
  .phone-icon {
    width: 86px;
    height: 86px;
    flex: none;
  }
  .phone-number {
    color: var(--paper);
    font-weight: 700;
    font-size: 108px;
    line-height: 1;
    letter-spacing: 1px;
  }
  .footer-band {
    position: absolute;
    left: 0;
    bottom: 0;
    width: 1040px;
    height: 170px;
  }
  .web-address {
    position: absolute;
    left: 0;
    right: 0;
    bottom: 48px;
    margin: 0;
    text-align: center;
    color: var(--paper);
    font-weight: 700;
    font-size: 72px;
    line-height: 1;
    letter-spacing: 1px;
  }
</style>
</head>
<body>
  <main class="decal">
    <header class="brand">
      <span class="brand-dot" aria-hidden="true"></span>
      <h1 class="brand-name">WEXLEY<br>FOOT &amp; ANKLE<br>HALVERTON</h1>
    </header>

    <p class="headline headline-service">PODIATRY</p>
    <p class="headline headline-specialty">FOOT &amp; ANKLE</p>
    <p class="headline headline-role">PHYSICIANS</p>

    <div class="phone-pill">
      <svg class="phone-icon" viewBox="0 0 100 100" aria-hidden="true">
        <circle cx="50" cy="50" r="48" fill="#1f1f1f"/>
        <path d="M34 26c3-2 6-1 7 2l4 9c1 2 0 4-2 5l-4 3c3 7 8 12 15 15l3-4c1-2 3-3 5-2l9 4c3 1 4 4 2 7l-3 4c-2 3-6 4-10 3-15-4-28-17-32-32-1-4 0-8 3-10z" fill="#f47e4a"/>
      </svg>
      <span class="phone-number">(877)555-0142</span>
    </div>

    <svg class="footer-band" viewBox="0 0 1040 170" aria-hidden="true">
      <path d="M0 70 Q60 10 120 0 L920 0 Q980 10 1040 70 L1040 170 L0 170 Z" fill="#27886f"/>
      <path d="M20 170 Q120 10 330 5 L710 5 Q920 10 1020 170 Z" fill="#55c3a7"/>
    </svg>
    <p class="web-address">www.StrideWellFeet.com</p>
  </main>
</body>
</html>
```